Commercial Office Fitout company needs a simple website

We need a website for our company Harbourline Fitouts (QLD) Pty Ltd. We are in the construction industry and we specialise in commercial office fitouts (partitions/glass/doors). Our company colours are black and silver. Please use our logo attached.
We only need an "about us" section, a "portfolio" section where we display some pictures of our work, and a "contact us" section. We would like our website to be simple, effective, professional and modern.

Industry/Entity Type

Construction

Number of Pages Required

1 page

```html
<!DOCTYPE html>
<html lang="en">
<head>
<meta charset="utf-8">
<title>Harbourline Fitouts (QLD) Pty Ltd</title>
<link href="https://fonts.googleapis.com/css2?family=Raleway:wght@200;300;400;600;700&display=swap" rel="stylesheet">
<style>
  :root {
    --ink: #2b2b2b;
    --ink-soft: #5a5a5a;
    --nav-muted: #8a8a8a;
    --dark-btn: #232323;
    --white: #ffffff;
    --light-band: #f7f7f7;
    --hero-top: #a7aaab;
    --hero-mid: #8d9092;
    --hero-low: #75787b;
  }
  * { box-sizing: border-box; margin: 0; padding: 0; }
  html, body {
    width: 1200px; height: 1200px; overflow: hidden;
    background: var(--white);
    font-family: "Raleway", sans-serif;
    color: var(--ink);
  }
  .page { position: relative; width: 1200px; height: 1200px; }

  .site-header {
    position: absolute; top: 0; left: 0; width: 1200px; height: 80px;
    background: var(--white);
  }
  .brand {
    position: absolute; left: 131px; top: 22px;
    display: flex; align-items: center; gap: 10px;
  }
  .brand-mark { width: 26px; height: 26px; background: var(--ink); }
  .brand-name {
    font-size: 13px; font-weight: 700; line-height: 16px;
    color: var(--ink); letter-spacing: 0.5px; text-transform: uppercase;
  }
  .main-nav { position: absolute; top: 0; left: 654px; height: 80px; display: flex; }
  .main-nav a {
    position: relative; display: block; height: 80px; line-height: 76px;
    padding: 0 12px; margin-right: 7px;
    font-size: 13px; font-weight: 300; color: var(--nav-muted);
    text-decoration: none; text-transform: uppercase;
  }
  .main-nav a.is-active { color: var(--ink); font-weight: 400; }
  .main-nav a.is-active::after {
    content: ""; position: absolute; left: 0; right: 0; bottom: 0;
    height: 3px; background: #111;
  }

  .hero {
    position: absolute; top: 80px; left: 0; width: 1200px; height: 477px;
    background: linear-gradient(180deg, var(--hero-top) 0%, var(--hero-mid) 55%, var(--hero-low) 100%);
  }
  .hero-photo {
    position: absolute; inset: 0;
    background: linear-gradient(90deg, rgba(110,135,110,0.35) 0%, rgba(150,150,150,0) 30%, rgba(190,195,198,0.25) 75%, rgba(170,175,178,0.2) 100%);
  }
  .hero-title {
    position: absolute; top: 214px; left: 0; width: 1200px; text-align: center;
    font-size: 48px; font-weight: 200; color: var(--white); letter-spacing: -0.5px;
  }
  .btn-dark {
    position: absolute; display: block; width: 138px; height: 40px;
    background: var(--dark-btn); color: var(--white);
    font-size: 9px; font-weight: 700; letter-spacing: 1.8px;
    text-align: center; line-height: 40px; text-decoration: none; text-transform: uppercase;
  }
  .hero .btn-dark { left: 534px; top: 312px; }

  .about {
    position: absolute; top: 557px; left: 0; width: 1200px; height: 482px;
    background: var(--light-band);
  }
  .section-title {
    position: absolute; left: 0; width: 1200px; text-align: center;
    font-size: 32px; font-weight: 300; color: var(--ink); letter-spacing: -0.5px;
  }
  .section-lead {
    position: absolute; left: 0; width: 1200px; text-align: center;
    font-size: 13px; font-weight: 400; color: var(--ink-soft);
  }
  .about .section-title { top: 38px; }
  .about .section-lead { top: 92px; }
  .about-col { position: absolute; top: 166px; width: 420px; }
  .about-col.left { left: 180px; }
  .about-col.right { left: 620px; }
  .about-col h3 { font-size: 14.5px; font-weight: 400; color: var(--ink); margin-bottom: 12px; }
  .about-col p { font-size: 11.6px; line-height: 19.2px; font-weight: 400; color: var(--ink-soft); white-space: nowrap; }
  .about .btn-dark { left: 531px; top: 393px; }

  .services { position: absolute; top: 1039px; left: 0; width: 1200px; height: 161px; background: var(--white); }
  .services .section-title { top: 40px; text-transform: uppercase; }
  .services .section-lead { top: 92px; }
</style>
</head>
<body>
<div class="page">
  <header class="site-header">
    <div class="brand">
      <span class="brand-mark"></span>
      <span class="brand-name">Harbourline Fitouts<br>(QLD) Pty Ltd</span>
    </div>
    <nav class="main-nav">
      <a href="#home" class="is-active">Home</a>
      <a href="#about">About</a>
      <a href="#services">Services</a>
      <a href="#portfolio">Portfolio</a>
      <a href="#contact">Contact</a>
    </nav>
  </header>

  <section class="hero" id="home">
    <div class="hero-photo" role="img" aria-label="Photo of a bright boardroom with a long table, office chairs, glass partitions and floor-to-ceiling windows over a city view"></div>
    <h1 class="hero-title">WE LOVE TO WORK WITH YOU</h1>
    <a class="btn-dark" href="#about">Start</a>
  </section>

  <section class="about" id="about">
    <h2 class="section-title">About Us</h2>
    <p class="section-lead">Neque porro quisquam est qui dolorem ipsum quia dolor sit amet, consectetur, adipisci velit...</p>
    <div class="about-col left">
      <h3>Who we are ?</h3>
      <p>Lorem Ipsum is simply dummy text of the printing and typesetting industry.<br>
      Lorem Ipsum has been the industry's standard dummy text ever since the<br>
      1500s, when an unknown printer took a galley of type and scrambled it to<br>
      make a type specimen book. It has survived not only five centuries, but a<br>
      lso the leap into electronic typesetting, remaining essentially unchanged.<br>
      It was popularised in the 1960s with the release of Letraset sheets containing<br>
      Lorem Ipsum passages, and more recently with desktop publishing software<br>
      like Aldus PageMaker including versions of Lorem Ipsum.</p>
    </div>
    <div class="about-col right">
      <h3>Who we are ?</h3>
      <p>Lorem Ipsum is simply dummy text of the printing and typesetting industry.<br>
      Lorem Ipsum has been the industry's standard dummy text ever since the<br>
      1500s, when an unknown printer took a galley of type and scrambled it to<br>
      make a type specimen book. It has survived not only five centuries, but a<br>
      lso the leap into electronic typesetting, remaining essentially unchanged.<br>
      It was popularised in the 1960s with the release of Letraset sheets containing<br>
      Lorem Ipsum passages, and more recently with desktop publishing software<br>
      like Aldus PageMaker including versions of Lorem Ipsum.</p>
    </div>
    <a class="btn-dark" href="#about">Read More</a>
  </section>

  <section class="services" id="services">
    <h2 class="section-title">Services</h2>
    <p class="section-lead">Neque porro quisquam est qui dolorem ipsum quia dolor sit amet, consectetur, adipisci velit...</p>
  </section>
</div>
</body>
</html>
```